Real Estate Investment Company Needs A Business Card Designed

I need a business card designed for my use. We are a real estate investment company based in Omaha, Nebraska that specializes in buying, rehabbing and selling single family and multifamily properties. Would love designs that incorporate our logo and colors

Industry/Entity Type

Business

Contact Information for Business Card

Marlow Pettigrew | President & CEO
4837 North 52nd Avenue, Ste 200
Omaha, NE 68214
(402) 555-7428
marlow@quillfenhomes.example
www.QuillfenHomes.example

Font styles to use
Serif

Colors
0255a3
3276b5

Requirements
Must have
• Our logo

```html
<!DOCTYPE html>
<html lang="en">
<head>
<meta charset="UTF-8">
<title>Quillfen Homes – Business Card</title>
<link rel="stylesheet" href="https://fonts.googleapis.com/css2?family=Montserrat:wght@700&family=Roboto:wght@400;500&display=swap">
<style>
  :root {
    --brand-deep: #0255a3;
    --brand-mid: #3276b5;
    --brand-light: #6aa6dc;
    --mark-grey: #9a9ea3;
    --paper: #ffffff;
    --backdrop: #e9ebee;
    --ink-light: #ffffff;
  }
  * { margin: 0; padding: 0; box-sizing: border-box; }
  html, body { width: 1200px; height: 800px; overflow: hidden; }
  body {
    background: var(--backdrop);
    display: flex;
    align-items: center;
    justify-content: center;
    gap: 40px;
    font-family: "Roboto", Arial, sans-serif;
  }
  .card {
    position: relative;
    width: 540px;
    height: 309px;
    background: var(--paper);
    box-shadow: 0 10px 30px rgba(0,0,0,0.18);
    overflow: hidden;
  }

  /* Front */
  .card-front { display: flex; align-items: center; justify-content: center; }
  .wordmark { display: flex; align-items: center; gap: 14px; }
  .wordmark-dot {
    width: 54px; height: 54px; border-radius: 50%;
    background: var(--brand-mid);
  }
  .wordmark-name {
    font-family: "Montserrat", Arial, sans-serif;
    font-weight: 700;
    font-size: 30px;
    letter-spacing: 1px;
    color: var(--brand-deep);
    line-height: 1;
  }

  /* Back */
  .card-back .back-field { position: absolute; inset: 0; }
  .back-content {
    position: absolute;
    left: 250px; top: 34px;
    color: var(--ink-light);
  }
  .back-name {
    font-family: "Montserrat", Arial, sans-serif;
    font-weight: 700;
    font-size: 24px;
    letter-spacing: 1px;
    line-height: 1;
    margin-bottom: 22px;
  }
  .person-name { font-size: 17px; font-weight: 500; line-height: 1.1; }
  .person-title { font-size: 12px; margin-bottom: 14px; }
  .contact-list { list-style: none; margin-bottom: 12px; }
  .contact-list li {
    display: flex; align-items: center; gap: 7px;
    font-size: 11.5px; line-height: 1.55;
  }
  .contact-icon { width: 12px; height: 12px; flex: none; }
  .address { font-size: 11.5px; line-height: 1.45; font-style: normal; }
</style>
</head>
<body>

  <section class="card card-front" aria-label="Card front">
    <div class="wordmark">
      <span class="wordmark-dot"></span>
      <span class="wordmark-name">QUILLFEN HOMES</span>
    </div>
  </section>

  <section class="card card-back" aria-label="Card back">
    <svg class="back-field" viewBox="0 0 540 309" preserveAspectRatio="none">
      <defs>
        <linearGradient id="backGradient" x1="0" y1="0" x2="1" y2="1">
          <stop offset="0" stop-color="var(--brand-light)"/>
          <stop offset="1" stop-color="var(--brand-deep)"/>
        </linearGradient>
      </defs>
      <rect width="540" height="309" fill="url(#backGradient)"/>
      <polygon points="0,150 0,309 250,309" fill="var(--paper)"/>
    </svg>

    <div class="back-content">
      <div class="back-name">QUILLFEN HOMES</div>
      <div class="person-name">Marlow Pettigrew</div>
      <div class="person-title">President &amp; CEO</div>
      <ul class="contact-list">
        <li>
          <svg class="contact-icon" viewBox="0 0 12 12"><circle cx="6" cy="6" r="5.4" fill="none" stroke="#fff" stroke-width="1"/><path d="M4 3.4l1 1-.6.8c.4.9 1.1 1.6 2 2l.8-.6 1 1-.7.9c-1.9-.3-3.5-1.9-3.8-3.8z" fill="#fff"/></svg>
          (402) 555-7428
        </li>
        <li>
          <svg class="contact-icon" viewBox="0 0 12 12"><circle cx="6" cy="6" r="5.4" fill="none" stroke="#fff" stroke-width="1"/><rect x="3.2" y="4" width="5.6" height="4" fill="none" stroke="#fff" stroke-width=".8"/><path d="M3.2 4L6 6.2 8.8 4" fill="none" stroke="#fff" stroke-width=".8"/></svg>
          marlow@quillfenhomes.example
        </li>
        <li>
          <svg class="contact-icon" viewBox="0 0 12 12"><circle cx="6" cy="6" r="5.4" fill="none" stroke="#fff" stroke-width="1"/><circle cx="6" cy="6" r="2.8" fill="none" stroke="#fff" stroke-width=".8"/><path d="M3.2 6h5.6M6 3.2v5.6" stroke="#fff" stroke-width=".6"/></svg>
          www.QuillfenHomes.example
        </li>
      </ul>
      <address class="address">
        4837 North 52nd Avenue, Ste 200<br>
        Omaha, NE 68214
      </address>
    </div>
  </section>

</body>
</html>
```